Design concept for BrightKestrel.com Support Page

We are about to launch a new support page for our www.brightkestrel.com service for photographers and visual artists. The service provides media management, cloud storage, promotional and secure distribution to our members.

The support page will include FAQs and video tutorials.

In particular we're looking for a header for this page that suggests the user is in the support area of our service - so perhaps an illustration that suggests support could look nice (perhaps repair man or doctor iconography). Something to give this area of our site a different look and something that looks both cool and friendly.

Currently the page looks distinctly sparse and undesigned (see attached screenshot) - something that could be remedied, we feel, by some subtle design enhancements that we can implement using CSS.

```html
<!DOCTYPE html>
<html lang="en">
<head>
<meta charset="utf-8">
<title>BrightKestrel – Frequently Asked Questions</title>
<link href="https://fonts.googleapis.com/css2?family=Open+Sans:ital,wght@0,300;0,400;0,600;0,700;1,300&display=swap" rel="stylesheet">
<style>
  :root {
    --orange: #f8a11c;
    --ink: #333333;
    --muted: #555555;
    --rule: #e4e4e4;
    --panel: #f2f2f2;
    --field: #ffffff;
    --placeholder: #b3b3b3;
    --footer: #050505;
    --footer-text: #dddddd;
  }
  * { box-sizing: border-box; margin: 0; padding: 0; }
  html, body { width: 800px; height: 1200px; overflow: hidden; background: #ffffff; }
  body { position: relative; font-family: "Open Sans", Arial, sans-serif; color: var(--ink); }
  .abs { position: absolute; }

  /* header */
  .site-header { left: 0; top: 0; width: 800px; height: 44px; background: #fff; }
  .brand { left: 83px; top: 10px; display: flex; align-items: center; gap: 7px; }
  .brand-mark { width: 18px; height: 18px; border-radius: 50%; background: var(--ink); }
  .brand-name { font-size: 19px; font-weight: 600; color: var(--ink); letter-spacing: -0.2px; }
  .header-divider { left: 242px; top: 10px; width: 1px; height: 24px; background: #bbbbbb; }
  .section-label { left: 250px; top: 13px; display: flex; align-items: center; gap: 8px; }
  .section-name { font-size: 12.5px; color: var(--ink); letter-spacing: -0.1px; }

  /* hero: support-area banner, warm wheat-field photo */
  .hero { left: 0; top: 44px; width: 800px; height: 185px;
    background: linear-gradient(100deg, #7c6a55 0%, #b49a78 25%, #d8c3a2 48%, #c3a887 70%, #6f5f4e 100%); }
  .hero-title { left: 0; top: 74px; width: 800px; text-align: center; font-size: 47px;
    font-weight: 300; font-style: italic; color: #ffffff; letter-spacing: -0.5px; }
  .search-box { left: 193px; top: 159px; width: 423px; height: 37px; background: rgba(255,255,255,0.35); }
  .search-input { left: 203px; top: 167px; width: 340px; height: 20px; background: #fff;
    font-size: 10px; font-style: italic; color: var(--placeholder); padding: 4px 9px; }
  .search-button { left: 543px; top: 167px; width: 64px; height: 20px; background: var(--orange);
    color: #fff; font-size: 10px; text-align: center; line-height: 20px; }

  /* section headings */
  .section-title { font-size: 22px; font-weight: 300; color: var(--ink); }
  .rule { height: 1px; background: var(--rule); }

  /* tutorials */
  .tutorial { width: 204px; border-bottom: 1px solid var(--rule); }
  .thumb { position: absolute; left: 0; top: 0; width: 204px; }
  .thumb-screen { background: linear-gradient(180deg, #e9e9e9 0%, #f6f6f6 45%, #cfcfcf 100%); }
  .thumb-dark { background: linear-gradient(180deg, #1e1e1e 0%, #f3f3f3 30%, #f3f3f3 85%, #2a2a2a 100%); }
  .thumb-photo { background: linear-gradient(160deg, #e8e8e8 0%, #8a7663 35%, #5b4b3e 70%, #2f2a26 100%); }
  .thumb-play { background: var(--orange); opacity: 0.92; }
  .play { position: absolute; left: 0; width: 204px; text-align: center; color: #fff; font-size: 10px; }
  .tutorial-title { position: absolute; left: 5px; font-size: 12px; font-weight: 400; color: var(--ink); }
  .tutorial-text { position: absolute; left: 5px; width: 200px; font-size: 9px; font-weight: 300; line-height: 13px; color: var(--muted); }
  .text-button { position: absolute; right: 0; width: 75px; height: 20px; background: var(--orange);
    color: #fff; font-size: 9px; font-weight: 300; text-align: center; line-height: 20px; }

  /* faq */
  .faq-item { left: 83px; width: 310px; background: var(--panel); }
  .faq-question { position: absolute; left: 12px; top: 5px; font-size: 9.5px; color: var(--ink); }
  .faq-toggle { position: absolute; right: 14px; top: 8px; }

  /* contact panel */
  .contact { left: 407px; top: 876px; width: 313px; height: 225px; background: var(--panel); }
  .contact-title { left: 420px; top: 882px; font-size: 21px; font-weight: 400; color: var(--ink); }
  .contact-text { left: 420px; top: 912px; width: 295px; font-size: 9.5px; line-height: 13px; color: var(--ink); }
  .field { left: 420px; width: 285px; background: var(--field); font-size: 9px; color: var(--placeholder); padding: 4px 7px; }
  .send-button { left: 623px; top: 1072px; width: 82px; height: 20px; background: var(--orange);
    color: #fff; font-size: 10px; display: flex; align-items: center; justify-content: center; gap: 6px; }

  /* footer */
  .site-footer { left: 0; top: 1121px; width: 800px; height: 79px; background: var(--footer); }
  .footer-links { left: 0; top: 1139px; width: 800px; text-align: center; font-size: 8px; color: var(--footer-text); }
  .footer-links span.sep { margin: 0 6px; color: #888; }
  .copyright { left: 0; top: 1163px; width: 800px; text-align: center; font-size: 8px; font-weight: 700; color: #fff; }
  .powered { left: 0; top: 1174px; width: 800px; text-align: center; font-size: 8px; color: #8a8a8a; }
</style>
</head>
<body>

<header class="site-header abs">
  <div class="brand abs"><span class="brand-mark"></span><span class="brand-name">BrightKestrel</span></div>
  <div class="header-divider abs"></div>
  <div class="section-label abs">
    <span class="section-name">Frequently Asked Questions</span>
    <svg width="16" height="14" viewBox="0 0 16 14" aria-hidden="true">
      <path d="M1 1h14v9H6l-3 3v-3H1z" fill="none" stroke="#f8a11c" stroke-width="1.2"/>
      <path d="M4 4.5h8M4 7h6" stroke="#f8a11c" stroke-width="1"/>
    </svg>
  </div>
</header>

<section class="hero abs" role="img" aria-label="Support banner photo: soft-focus wheat stalks in warm evening light"></section>
<h1 class="hero-title abs">We’ve got all the answers...</h1>
<div class="search-box abs"></div>
<div class="search-input abs">What’s your question?</div>
<div class="search-button abs">Search</div>

<h2 class="section-title abs" style="left:81px;top:240px;">Video Tutorials</h2>
<div class="rule abs" style="left:80px;top:271px;width:640px;"></div>

<article class="tutorial abs" style="left:80px;top:285px;height:248px;">
  <div class="thumb thumb-play" style="height:98px;" role="img" aria-label="Screenshot of the upload screen with play overlay">
    <svg style="position:absolute;left:94px;top:38px;" width="16" height="16" viewBox="0 0 16 16" aria-hidden="true">
      <path d="M3 1l11 7-11 7z" fill="none" stroke="#fff" stroke-width="1.2"/>
    </svg>
    <div class="play" style="top:56px;">Play Video</div>
  </div>
  <h3 class="tutorial-title" style="top:102px;">Uploading Files</h3>
  <p class="tutorial-text" style="top:126px;">In this tutorial we’ll see how to upload your files using FTP.</p>
  <div class="text-button" style="top:216px;">Text Version</div>
</article>

<article class="tutorial abs" style="left:297px;top:285px;height:248px;">
  <div class="thumb thumb-screen" style="height:98px;" role="img" aria-label="Screenshot of the publishing screen"></div>
  <h3 class="tutorial-title" style="top:102px;">Publishing Files</h3>
  <p class="tutorial-text" style="top:126px;">In this tutorial we’ll see how to publish your files once they’ve been uploaded</p>
  <div class="text-button" style="top:216px;">Text Version</div>
</article>

<article class="tutorial abs" style="left:515px;top:285px;height:248px;">
  <div class="thumb thumb-dark" style="height:98px;" role="img" aria-label="Screenshot of the file information editor"></div>
  <h3 class="tutorial-title" style="top:102px;">Editing File Information</h3>
  <p class="tutorial-text" style="top:124px;">In this tutorial we’ll see how to edit file information onced they’ve been published.</p>
  <div class="text-button" style="top:216px;">Text Version</div>
</article>

<article class="tutorial abs" style="left:80px;top:541px;height:251px;border-bottom:none;">
  <div class="thumb thumb-photo" style="height:103px;" role="img" aria-label="Screenshot of the sharing page with a camera photo"></div>
  <h3 class="tutorial-title" style="top:107px;">Sharing Files</h3>
  <p class="tutorial-text" style="top:131px;">In this tutorial we’ll see how to share your files.</p>
  <div class="text-button" style="top:222px;">Text Version</div>
</article>

<h2 class="section-title abs" style="left:84px;top:810px;">Other Frequently Asked Questions</h2>
<div class="rule abs" style="left:83px;top:856px;width:310px;"></div>

<div class="faq-item abs" style="top:876px;height:164px;">
  <p class="faq-question">Lorem ipsum dolor sit amet, consectetur adipiscing elit?</p>
  <svg class="faq-toggle" width="14" height="8" viewBox="0 0 14 8" aria-hidden="true"><path d="M0 8L7 0l7 8z" fill="#333"/></svg>
</div>
<div class="faq-item abs" style="top:1048px;height:24px;">
  <p class="faq-question">Lorem ipsum dolor sit amet, consectetur adipiscing elit?</p>
  <svg class="faq-toggle" width="14" height="8" viewBox="0 0 14 8" aria-hidden="true"><path d="M0 0l7 8 7-8z" fill="#333"/></svg>
</div>
<div class="faq-item abs" style="top:1077px;height:24px;">
  <p class="faq-question">Lorem ipsum dolor sit amet, consectetur adipiscing elit?</p>
  <svg class="faq-toggle" width="14" height="8" viewBox="0 0 14 8" aria-hidden="true"><path d="M0 0l7 8 7-8z" fill="#333"/></svg>
</div>

<aside class="contact abs"></aside>
<h2 class="contact-title abs">Need an answer?</h2>
<p class="contact-text abs">We’re always looking for ways to help you. So if you’ve got a question that you need answers to, send us a message!</p>
<div class="field abs" style="top:949px;height:19px;">Name</div>
<div class="field abs" style="top:976px;height:19px;">Email Address</div>
<div class="field abs" style="top:1002px;height:61px;">What’s your question?</div>
<div class="send-button abs">Get answers
  <svg width="14" height="10" viewBox="0 0 14 10" aria-hidden="true"><rect x="0.5" y="0.5" width="13" height="9" fill="none" stroke="#fff"/><path d="M0.5 0.5L7 6l6.5-5.5" fill="none" stroke="#fff"/></svg>
</div>

<footer class="site-footer abs"></footer>
<nav class="footer-links abs">Home<span class="sep">•</span>Contact Us<span class="sep">•</span>Affiliate Program<span class="sep">•</span>Privacy Policy<span class="sep">•</span>Site Terms and Conditions<span class="sep">•</span>About Us</nav>
<p class="copyright abs">© Copyright 2014 Northwind Imaging Pte Ltd. All rights reserved.</p>
<p class="powered abs">Powered by BrightKestrel</p>

</body>
</html>
```